Driftwood Coatings of Central Florida, LLC. Start-up painting business needs a professional web desig

We have a start up painting business that would like to reach/focus on commercial clients like building contractors, HOA's, apartment complexes, etc.. We would like a residential aspect to the web design as well. We have an existing website at "trydriftwoodcoatings.com" with usable content. Have logo and color scheme attached. Use provided website ONLY as template. Add commercial services page. Can type own content when needed.

```html
<!DOCTYPE html>
<html lang="en">
<head>
<meta charset="utf-8">
<title>Driftwood Coatings of Central Florida, LLC</title>
<link href="https://fonts.googleapis.com/css2?family=Lato:wght@400;700;900&family=Oswald:wght@400&family=Kaushan+Script&display=swap" rel="stylesheet">
<style>
:root{
  --orange:#e37b2f;
  --olive:#7b7f05;
  --tan:#bca583;
  --slate:#6a6a6a;
  --ink:#333;
  --beige:#ddd0bf;
  --page:#f3f3f3;
  --dark:#2b2b2b;
  --white:#fff;
  --red:#b8323a;
}
*{margin:0;padding:0;box-sizing:border-box}
html,body{width:845px;height:1200px;overflow:hidden}
body{font-family:"Lato",sans-serif;color:var(--ink);background:var(--page);position:relative}
.abs{position:absolute}
.header{left:0;top:0;width:845px;height:85px;background:var(--white)}
.phone{top:34px;font-size:17px;font-weight:700;color:#3a3a3a;display:flex;align-items:center;gap:7px}
.brand{left:322px;top:28px;width:200px;text-align:center;font-size:15px;font-weight:900;color:var(--olive);line-height:1.2}
.nav{left:0;top:85px;width:845px;height:33px;background:var(--orange)}
.nav a{position:absolute;top:9px;color:var(--white);font-size:12px;font-weight:700;text-decoration:none}
.hero{left:0;top:118px;width:845px;height:332px;background:#3a3a3a}
.video{left:92px;top:118px;width:450px;height:233px;background:linear-gradient(135deg,#f4f2ee 0%,#e6e2dc 45%,#7aa4d8 100%)}
.tagline{left:106px;top:140px;font-family:"Kaushan Script",cursive;font-size:21px;color:var(--olive);line-height:30px}
.tagline span{display:block;padding-left:56px}
.play{left:299px;top:224px;width:36px;height:26px;background:rgba(40,40,40,.6);border-radius:3px}
.controls{left:92px;top:351px;width:450px;height:21px;background:#1d1f24}
.call{left:92px;top:372px;width:450px;height:78px;background:var(--beige);text-align:center;font-family:"Oswald",sans-serif;font-size:17px;color:#333;padding-top:15px;line-height:26px}
.estimate{left:542px;top:118px;width:210px;height:332px;background:var(--orange);color:var(--white)}
.estimate-head{height:34px;background:var(--olive);font-size:15px;font-weight:700;text-align:center;padding-top:9px}
.estimate h3{font-size:13.5px;text-align:center;margin-top:16px}
.estimate p{font-size:8.6px;text-align:center;line-height:11px;padding:4px 10px 0}
.field{position:absolute;left:12px;width:186px;height:17px;background:var(--white);border:1px solid #ccc;border-radius:2px;font-size:8.5px;color:#444;padding:3px 6px}
.submit{position:absolute;left:12px;top:293px;width:92px;height:23px;background:var(--olive);border-radius:3px;font-size:12px;font-weight:700;text-align:center;padding-top:4px}
.welcome{left:93px;top:476px;font-size:14px;font-weight:700;color:#333}
.welcome em{font-style:normal;color:var(--orange)}
.rule{left:93px;top:497px;width:262px;height:1px;background:linear-gradient(90deg,#bbb,transparent)}
.copy{left:93px;top:509px;width:435px;font-size:10.3px;line-height:14.8px;color:#444}
.copy p{margin-bottom:7px}
.btn{left:92px;top:661px;width:68px;height:23px;background:var(--olive);color:var(--white);font-size:10px;font-weight:700;text-align:center;padding-top:6px;border-radius:2px}
.specials{left:567px;top:478px;width:187px;height:205px;background:linear-gradient(180deg,var(--red) 0%,#c23a42 55%,#d7cfc4 75%,#bfb09b 100%)}
.specials-text{left:567px;top:533px;width:187px;text-align:center;color:var(--white);font-size:15px;font-weight:700;font-style:italic;text-decoration:underline;line-height:22px}
.divider{left:0;top:711px;width:845px;height:1px;background:#d6d6d6}
.svc-title{left:350px;top:714px;width:145px;height:30px;background:#e9e2d6;text-align:center;font-size:15px;font-weight:700;padding-top:6px}
.svc-title em{font-style:normal;color:var(--orange)}
.card{width:139px;height:128px;top:812px;border-radius:0 0 6px 6px;color:var(--white);text-align:center}
.card h4{font-size:10px;font-weight:700;margin-top:50px}
.card p{font-size:8.3px;font-weight:700;line-height:11px;margin-top:6px}
.card a{display:inline-block;margin-top:8px;font-size:9.5px;font-weight:700;color:var(--white)}
.thumb{width:82px;height:82px;top:770px;border-radius:50%;border:3px solid var(--white)}
.footer{left:0;top:966px;width:845px;height:234px;background:var(--dark);color:var(--white)}
.fnav{position:absolute;left:0;top:18px;width:845px;text-align:center;font-size:9.5px;font-weight:700}
.fnav span{margin:0 7px}
.fline{position:absolute;height:1px;background:#555}
.fcol{position:absolute;font-size:12.5px;font-weight:700}
.email-in{position:absolute;left:194px;top:77px;width:221px;height:26px;background:var(--white);font-size:8px;color:#999;padding:8px 8px}
.email-btn{position:absolute;left:420px;top:77px;width:58px;height:26px;background:var(--orange);font-size:11px;font-weight:700;text-align:center;padding-top:6px}
.vline{position:absolute;width:1px;background:#555}
.social{position:absolute;top:79px;width:22px;height:22px;border-radius:50%;background:#3f6b83}
.info{position:absolute;font-size:9.5px;line-height:15px}
.fbrand{position:absolute;left:528px;top:130px;width:80px;font-size:10px;font-weight:900;color:#888;text-align:center;line-height:13px}
.legal{position:absolute;left:0;top:209px;width:845px;text-align:center;font-size:9px;font-weight:700}
</style>
</head>
<body>
<header class="abs header">
  <div class="abs phone" style="left:92px">
    <svg width="18" height="18" viewBox="0 0 18 18"><circle cx="9" cy="9" r="8" fill="none" stroke="#7b7f05" stroke-width="1.5"/><path d="M6 5c.7-.7 1.3 0 1.7.8.3.6 0 1-.4 1.4.5 1 1.2 1.8 2.2 2.3.4-.4.8-.7 1.4-.4.8.4 1.5 1 .8 1.7-1.8 1.7-7.3-3.8-5.7-5.8z" fill="#7b7f05"/></svg>
    +1.863-555-0142</div>
  <div class="abs brand">Driftwood Coatings</div>
  <div class="abs phone" style="left:603px">
    <svg width="18" height="18" viewBox="0 0 18 18"><circle cx="9" cy="9" r="8" fill="none" stroke="#7b7f05" stroke-width="1.5"/><path d="M6 5c.7-.7 1.3 0 1.7.8.3.6 0 1-.4 1.4.5 1 1.2 1.8 2.2 2.3.4-.4.8-.7 1.4-.4.8.4 1.5 1 .8 1.7-1.8 1.7-7.3-3.8-5.7-5.8z" fill="#7b7f05"/></svg>
    +1.863-555-0178</div>
</header>

<nav class="abs nav">
  <a style="left:123px">HOME</a>
  <a style="left:235px">ABOUT US</a>
  <a style="left:558px">SERVICES</a>
  <a style="left:687px">CONTACT US</a>
</nav>

<section class="abs hero"></section>
<div class="abs video" role="img" aria-label="Video still of a young couple sitting on the floor with a paint roller beside a ladder"></div>
<div class="abs tagline">Where Dreams<span>Meet Reality</span></div>
<div class="abs play"><svg width="36" height="26" viewBox="0 0 36 26"><path d="M14 7l10 6-10 6z" fill="#fff"/></svg></div>
<div class="abs controls">
  <svg width="450" height="21" viewBox="0 0 450 21">
    <rect x="6" y="4" width="18" height="13" rx="2" fill="#5a6f9c"/><path d="M12 7l6 3.5-6 3.5z" fill="#fff"/>
    <rect x="35" y="8" width="135" height="5" rx="2.5" fill="#d8d8d8"/><rect x="35" y="8" width="32" height="5" rx="2.5" fill="#7a8db8"/><circle cx="67" cy="10.5" r="3.5" fill="#fff"/>
    <text x="175" y="14" font-family="Lato,sans-serif" font-size="7" fill="#ddd">147 / 12:35</text>
    <rect x="387" y="4" width="17" height="13" rx="2" fill="#5a6f9c"/><rect x="410" y="4" width="17" height="13" rx="2" fill="#5a6f9c"/><rect x="432" y="4" width="16" height="13" rx="2" fill="#5a6f9c"/>
  </svg>
</div>
<div class="abs call">Call today to schedule your appointment and free estimate.<br>We can't wait to hear from you!&nbsp; +1.863-555-0142</div>

<aside class="abs estimate">
  <div class="estimate-head">SCHEDULE FREE ESTIMATE</div>
  <h3>How to Schedule an Estimae</h3>
  <p>Requesting an estimate online is very simple and easy. Fill out the Form below and we will send you a rough quote to your email. We may also call you if we have any more questions.</p>
  <div class="field" style="top:138px">Name:</div>
  <div class="field" style="top:162px">Email:</div>
  <div class="field" style="top:185px">Phone:</div>
  <div class="field" style="top:209px;height:39px">Decribe what needs to be done.</div>
  <div style="position:absolute;left:12px;top:255px;font-size:8.5px">Please type the following</div>
  <div class="field" style="top:268px">ac2gH</div>
  <div class="submit">Submit Now</div>
</aside>

<h2 class="abs welcome"><em>WELCOME TO</em> DRIFTWOOD COATINGS OF CENTRAL FLORIDA, LLC.</h2>
<div class="abs rule"></div>
<div class="abs copy">
  <p>Lorem ipsum dolor sit amet, consectetuer adipiscing elit, sed diam nonummy nibh euismod tincidunt ut laoreet dolore magna aliquam erat volutpat. Ut wisi enim ad minim veniam, quis nostrud exerci tation ullamcorper suscipit lobortis nisl ut aliquip ex ea commodo consequat. Duis autem vel eum iriure dolor in hendrerit in vulputate velit esse molestie consequat, vel illum dolore eu feugiat nulla facilisis at vero eros et accumsan et iusto odio dignissim qui blandit praesent luptatum zzril delenit augue duis dolore te feugait nulla facilisi.</p>
  <p>Lorem ipsum dolor sit amet, consectetuer adipiscing elit, sed diam nonummy nibh euismod tincidunt ut laoreet dolore magna aliquam erat volutpat. Ut wisi enim ad minim veniam, quis nostrud exerci tation ullamcorper suscipit lobortis nisl ut aliquip ex ea commodo consequat.</p>
</div>
<div class="abs btn">Read More</div>
<div class="abs specials" role="img" aria-label="Red painted wall with a white sofa on a wooden floor"></div>
<div class="abs specials-text">CHECK OUT<br>OUR SPECIALS!</div>

<div class="abs divider"></div>
<h2 class="abs svc-title"><em>OUR</em> SERVICES</h2>

<div class="abs card" style="left:92px;background:var(--orange)"><h4>COMMERCIAL SERVICES</h4><p>Lorem ipsum dolor sit a consecte<br>adipiscing Lorem ipsum...</p><a>Read more</a></div>
<div class="abs card" style="left:266px;background:var(--olive)"><h4>RESIDENTIAL SERVICES</h4><p>Lorem ipsum dolor sit a consecte<br>adipiscing Lorem ipsum...</p><a>Read more</a></div>
<div class="abs card" style="left:440px;background:var(--tan)"><h4>INTERIOR SERVICES</h4><p>Lorem ipsum dolor sit a consecte<br>adipiscing Lorem ipsum...</p><a>Read more</a></div>
<div class="abs card" style="left:615px;background:var(--slate)"><h4>EXTERIOR SERVICES</h4><p>Lorem ipsum dolor sit a consecte<br>adipiscing Lorem ipsum...</p><a>Read more</a></div>
<div class="abs thumb" style="left:120px;background:linear-gradient(180deg,#7d8a93,#c34a2c)" role="img" aria-label="Worker on a lift painting a commercial building"></div>
<div class="abs thumb" style="left:294px;background:linear-gradient(180deg,#3a86d6,#e9eef4)" role="img" aria-label="Couple holding paint rollers"></div>
<div class="abs thumb" style="left:468px;background:linear-gradient(135deg,#f1dca7,#b98a52)" role="img" aria-label="Hand painting a wall with a brush"></div>
<div class="abs thumb" style="left:643px;background:linear-gradient(180deg,#eef0ea,#5a7a4c)" role="img" aria-label="Painter on a ladder painting a house exterior"></div>

<footer class="abs footer">
  <div class="fnav"><span>HOME</span>•<span>ABOUT US</span>•<span>SERVICES</span>•<span>CONTACT US</span></div>
  <div class="fline" style="left:108px;top:42px;width:629px"></div>
  <div class="fcol" style="left:195px;top:55px">Sign up for Newsletter</div>
  <div class="email-in">Enter Your Email</div>
  <div class="email-btn">SUBMIT</div>
  <div class="vline" style="left:503px;top:60px;height:50px"></div>
  <div class="fcol" style="left:531px;top:55px">Follow Us On</div>
  <div class="social" style="left:531px"></div>
  <div class="social" style="left:559px"></div>
  <div class="social" style="left:587px"></div>
  <div class="social" style="left:615px;background:#a33b32"></div>
  <div class="fline" style="left:195px;top:124px;width:455px"></div>
  <svg style="position:absolute;left:193px;top:142px" width="11" height="15" viewBox="0 0 11 15"><path d="M5.5 0A5.5 5.5 0 0 0 0 5.5C0 9.5 5.5 15 5.5 15S11 9.5 11 5.5A5.5 5.5 0 0 0 5.5 0z" fill="#e37b2f"/><circle cx="5.5" cy="5.5" r="2" fill="#2b2b2b"/></svg>
  <div class="info" style="left:212px;top:139px">1187 Heron Bay Loop<br>Lakeland, FL<br>33801</div>
  <svg style="position:absolute;left:375px;top:142px" width="14" height="14" viewBox="0 0 14 14"><path d="M3 1c1-1 2 0 2.6 1.2.4.9 0 1.5-.6 2 .8 1.6 1.9 2.8 3.4 3.6.6-.6 1.2-1 2.1-.6 1.2.6 2.3 1.5 1.2 2.6C9 13 .5 4.4 3 1z" fill="#e37b2f"/></svg>
  <div class="info" style="left:396px;top:141px;font-size:11px">+1.863-555-0178</div>
  <svg style="position:absolute;left:336px;top:168px" width="15" height="10" viewBox="0 0 15 10"><rect width="15" height="10" fill="#e37b2f"/><path d="M0 0l7.5 5.5L15 0" fill="none" stroke="#2b2b2b" stroke-width="1"/></svg>
  <div class="info" style="left:355px;top:165px">info@trydriftwoodcoatings.com</div>
  <div class="vline" style="left:503px;top:135px;height:50px"></div>
  <div class="fbrand">Driftwood Coatings</div>
  <div class="fline" style="left:195px;top:199px;width:455px"></div>
  <div class="legal">© 2015 Marcus Reed. All Rights Reserved.</div>
</footer>
</body>
</html>
```